Church Equipping Classes Needing Printed Banner

We are looking for a printed Banner that will be 24x36. I attached and example on the brief. Please visit out website at velunbrook.org to see what we do.

Harvest Lantern is the name of our equipping process. It has four classes:

Harvest Lantern - The end goal is to Connect
Oakheart Pathway - Our end goal is for people to get the Culture of the Kingdom
Table of Embers - End goal is they would find Community
Missions - Wayfarer Sendout End goal is they would go on missions.

Our mission is teaching people and reaching nations with the message of Freedom. Galatians 5:1

The concept/idea behind the banner is to communicate this mission as well as the four classes.

Logos to incorporate:
Attached

Please let me know of anything you need to help. We would like our logo on everything but an idea to incorporate the whole concept of Harvest Lantern. Then each class represented as well in that concept. These four classes run each month at our church and each one will have it's on banner and book cover, etc.

The text that the banner should contain is:

Teaching people, Reaching Nations with Freedom.
Galatians 5:1

- Encounter the radical grace & supernatural love of your Heavenly Father!
- Learn something practical and relevant that's guaranteed to work on Sunday AND Monday!
- Connect with others like you- people walking from brokenness into raw grace & unconditional love!
- Discover how you, right now, can change the world!

Target Market(s)

Church members and people outside the church looking for an equipping process.

Industry/Entity Type

Church

Font styles to use
Serif
Sans Serif
Decorative
Script

Colors

Designer to choose colors to be used in the design.

Requirements
Must have
• Logo of our church. Overall concept of Harvest Lantern throughout and each class represented uniquely in the concept. Harvest Lantern is the overall process, but it is also the first class.

```html
<!DOCTYPE html>
<html lang="en">
<head>
<meta charset="utf-8">
<title>Harvest Lantern Banner</title>
<link rel="stylesheet" href="https://fonts.googleapis.com/css2?family=Bebas+Neue&family=Marcellus&family=Marcellus+SC&display=swap">
<style>
  :root {
    --page-bg: #f2f2f2;
    --frame-light: #d9dcdd;
    --frame-dark: #8b9092;
    --teal-top: #2f93a8;
    --teal-mid: #216f80;
    --teal-deep: #1b5562;
    --line-teal: #4fb3c4;
    --white: #ffffff;
    --ink: #0c0f10;
    --class-connect: #8fc2c4;
    --class-culture: #3f7c56;
    --class-community: #3a5f8d;
    --class-missions: #4a4458;
    --badge-teal: #1690a8;
    --verse-grey: #a9c4ca;
  }
  html, body {
    margin: 0;
    width: 1200px;
    height: 1200px;
    overflow: hidden;
    background: var(--page-bg);
  }
  .canvas {
    position: relative;
    width: 1200px;
    height: 1200px;
  }
  .banner {
    position: absolute;
    left: 180px;
    top: 12px;
    width: 840px;
    height: 1176px;
    display: block;
  }
  .title-script { font-family: "Marcellus", serif; }
  .title-caps { font-family: "Marcellus SC", serif; }
  .sans { font-family: "Bebas Neue", sans-serif; }
</style>
</head>
<body>
<div class="canvas">
  <svg class="banner" viewBox="0 0 840 1176" xmlns="http://www.w3.org/2000/svg">
    <defs>
      <linearGradient id="frameMetal" x1="0" y1="0" x2="1" y2="1">
        <stop offset="0" stop-color="var(--frame-dark)"/>
        <stop offset="0.35" stop-color="var(--frame-light)"/>
        <stop offset="0.65" stop-color="var(--frame-dark)"/>
        <stop offset="1" stop-color="var(--frame-light)"/>
      </linearGradient>
      <linearGradient id="panelTeal" x1="0" y1="0" x2="0" y2="1">
        <stop offset="0" stop-color="var(--teal-top)"/>
        <stop offset="0.55" stop-color="var(--teal-mid)"/>
        <stop offset="1" stop-color="var(--teal-deep)"/>
      </linearGradient>
      <linearGradient id="photoTones" x1="0" y1="0" x2="0" y2="1">
        <stop offset="0" stop-color="#f7e7a6"/>
        <stop offset="0.3" stop-color="#fbf5dc"/>
        <stop offset="0.55" stop-color="#d8e6ea"/>
        <stop offset="1" stop-color="#b9d3db"/>
      </linearGradient>
      <clipPath id="panelClip">
        <rect x="31" y="24" width="780" height="1131" rx="12"/>
      </clipPath>
    </defs>

    <!-- frame -->
    <rect class="banner-frame" x="0" y="0" width="840" height="1176" fill="url(#frameMetal)"/>
    <rect class="banner-panel" x="31" y="24" width="780" height="1131" rx="12" fill="url(#panelTeal)"/>

    <!-- hero photo area -->
    <g clip-path="url(#panelClip)">
      <circle class="hero-photo" cx="421" cy="260" r="345" fill="url(#photoTones)"
              role="img" aria-label="Photo of a couple on a beach at sunrise, arms raised toward the sea"/>
    </g>

    <!-- church name badge -->
    <g class="church-badge">
      <rect x="448" y="508" width="285" height="61" rx="6" fill="var(--badge-teal)" stroke="var(--white)" stroke-width="1.5"/>
      <circle cx="482" cy="538" r="16" fill="none" stroke="var(--white)" stroke-width="2"/>
      <text class="sans" x="510" y="552" font-size="38" fill="var(--white)" letter-spacing="1">VELUNBROOK</text>
    </g>

    <!-- staff lines -->
    <g class="title-lines" stroke="var(--line-teal)" stroke-width="1.2" opacity="0.7">
      <line x1="45" y1="695" x2="811" y2="695"/>
      <line x1="45" y1="725" x2="811" y2="725"/>
      <line x1="200" y1="755" x2="811" y2="755"/>
      <line x1="250" y1="782" x2="811" y2="782"/>
      <line x1="270" y1="812" x2="811" y2="812"/>
      <line x1="31" y1="1000" x2="380" y2="1000"/>
    </g>

    <!-- title -->
    <text class="title-script" x="48" y="718" font-size="150" fill="var(--white)">Harvest</text>
    <text class="title-caps" x="804" y="853" font-size="112" fill="var(--white)" text-anchor="end">LANTERN</text>

    <!-- class drops -->
    <g class="class-drops">
      <g class="class-drop class-connect">
        <path d="M129,808 Q183,796 189,754 L189,868 A60 60 0 1 1 129,808 Z" fill="var(--ink)"/>
        <circle cx="129" cy="868" r="51" fill="var(--class-connect)"/>
        <text class="sans" x="129" y="864" font-size="21" fill="var(--white)" text-anchor="middle">HARVEST</text>
        <text class="sans" x="129" y="888" font-size="21" fill="var(--white)" text-anchor="middle">LANTERN</text>
      </g>
      <g class="class-drop class-culture">
        <path d="M265,851 Q319,839 325,797 L325,911 A60 60 0 1 1 265,851 Z" fill="var(--ink)" transform="scale(-1,1) translate(-530,0)"/>
        <circle cx="265" cy="911" r="51" fill="var(--class-culture)"/>
        <text class="sans" x="265" y="907" font-size="21" fill="var(--white)" text-anchor="middle">OAKHEART</text>
        <text class="sans" x="265" y="931" font-size="21" fill="var(--white)" text-anchor="middle">PATHWAY</text>
      </g>
      <g class="class-drop class-community">
        <circle cx="129" cy="1002" r="60" fill="var(--ink)"/>
        <circle cx="129" cy="1002" r="51" fill="var(--class-community)"/>
        <text class="sans" x="129" y="998" font-size="21" fill="var(--white)" text-anchor="middle">TABLE</text>
        <text class="sans" x="129" y="1022" font-size="21" fill="var(--white)" text-anchor="middle">OF EMBERS</text>
      </g>
      <g class="class-drop class-missions">
        <circle cx="265" cy="1049" r="60" fill="var(--ink)"/>
        <circle cx="265" cy="1049" r="51" fill="var(--class-missions)"/>
        <text class="sans" x="265" y="1045" font-size="21" fill="var(--white)" text-anchor="middle">WAYFARER</text>
        <text class="sans" x="265" y="1069" font-size="21" fill="var(--white)" text-anchor="middle">SENDOUT</text>
      </g>
    </g>

    <!-- mission statement -->
    <g class="mission" fill="var(--white)" text-anchor="end" font-size="41">
      <text class="sans" x="800" y="937">TEACHING PEOPLE</text>
      <text class="sans" x="800" y="985">AND REACHING NATIONS</text>
      <text class="sans" x="800" y="1032">WITH THE MESSAGE</text>
      <text class="sans" x="800" y="1079">OF FREEDOM.</text>
    </g>
    <text class="sans verse" x="800" y="1127" font-size="20" fill="var(--verse-grey)" text-anchor="end">GALATIANS 5:1</text>
  </svg>
</div>
</body>
</html>
```